Business card design needed

We are a start up Mobile Vet Clinic.
We will be servicing an are that cover the Gladstone Region Shire.
Bookings will be made via the number listed or email address.
Travel will be charged

Target Market(s)

Pet Owners

Industry/Entity Type

Business

Contact Information for Business Card

BRAMLEY MOBILE VET
Tavestock Pty Ltd
Nora Batterby BVSc
27 Harwick St
Wrenfield TVL 4719

PH: 0738214069 Fax: 0738214552 email: bmvet@tallowmail.com

Logo styles of interest
Pictorial/Combination Logo

```html
<!DOCTYPE html>
<html lang="en">
<head>
<meta charset="utf-8">
<title>Bramley Mobile Vet – Business Card</title>
<link rel="stylesheet" href="https://fonts.googleapis.com/css2?family=Noto+Sans:wght@400;700&display=swap">
<style>
  :root {
    --page: #e9e9e9;
    --card: #000000;
    --panel: #ffffff;
    --ink: #ffffff;
    --accent: #e8262b;
  }
  * { margin: 0; padding: 0; box-sizing: border-box; }
  html, body {
    width: 978px;
    height: 1200px;
    overflow: hidden;
    background: var(--page);
  }
  .business-card {
    position: absolute;
    left: 0;
    top: 317px;
    width: 978px;
    height: 566px;
    background: var(--card);
    color: var(--ink);
    font-family: "Noto Sans", Verdana, sans-serif;
    overflow: hidden;
  }
  .paw-panel {
    position: absolute;
    left: 0;
    top: 0;
    width: 978px;
    height: 566px;
  }
  .brand-dot {
    position: absolute;
    left: 246px;
    top: 74px;
    width: 106px;
    height: 106px;
    border-radius: 50%;
    background: var(--accent);
  }
  .brand-name {
    position: absolute;
    left: 378px;
    top: 78px;
    font-weight: 700;
    line-height: 1;
    white-space: nowrap;
  }
  .brand-name .line-main {
    display: block;
    font-size: 60px;
    letter-spacing: -0.5px;
  }
  .brand-name .line-sub {
    display: block;
    font-size: 48px;
    margin-top: 6px;
  }
  .contact {
    position: absolute;
    left: 300px;
    width: 602px;
    text-align: center;
    line-height: 1;
    white-space: nowrap;
  }
  .holder-name {
    top: 272px;
    font-size: 62px;
    font-weight: 400;
    letter-spacing: 3px;
  }
  .address {
    top: 369px;
    font-size: 26px;
    letter-spacing: 2px;
  }
  .phones {
    top: 0;
    height: 0;
  }
  .phones span {
    position: absolute;
    font-size: 23px;
    letter-spacing: 1.5px;
    line-height: 1;
  }
  .phones .phone { left: 52px; top: 425px; }
  .phones .fax { left: 308px; top: 418px; }
  .email {
    top: 469px;
    font-size: 25px;
    letter-spacing: 1px;
    text-decoration: underline;
    text-underline-offset: 4px;
  }
</style>
</head>
<body>
  <section class="business-card">
    <svg class="paw-panel" viewBox="0 0 978 566">
      <polygon role="img" aria-label="Column of black paw prints on white" points="0,0 129,0 257,286 115,566 0,566" fill="var(--panel)"/>
    </svg>

    <span class="brand-dot"></span>
    <p class="brand-name">
      <span class="line-main">BRAMLEY MOBILE</span>
      <span class="line-sub">VET Tavestock Pty Ltd</span>
    </p>

    <h1 class="contact holder-name">Nora Batterby</h1>
    <p class="contact address">BVSc 27 Harwick St Wrenfield TVL 4719</p>
    <p class="contact phones">
      <span class="phone">PH: 0738214069</span>
      <span class="fax">Fax: 0738214552</span>
    </p>
    <p class="contact email">email: bmvet@tallowmail.com</p>
  </section>
</body>
</html>
```